Speisekarten-Design für Bistro und Café
Zielgruppe
Bistro und Café in der Eifel mit gemischten Publikum . Aber eher jünger modernere Gäste . Wir sind auch ein junges Team .
Bieten Frühstück, kaffee und Kuchen, Waffeln Burger, und Cocktails , Wein und co an
Aufgabenstellung
Gerne etwas modernes und Frisches in DIN a 4 im Anhang wie es aussehen könnte in die Richtung wäre es super . Gerne bunt und modern .

```html
<!DOCTYPE html>
<html lang="de">
<head>
<meta charset="utf-8">
<title>Bistro &amp; Café Zum Hammerwerk – Speisekarte</title>
<link rel="stylesheet" href="https://fonts.googleapis.com/css2?family=Dela+Gothic+One&family=Montserrat:wght@400;600;700&family=Sacramento&display=swap">
<style>
:root{
  --bg:#e8e5de;
  --paper:#ffffff;
  --ink:#141414;
  --muted:#777;
  --green:#7ab648;
  --orange:#f0a028;
  --yellow:#f2cf17;
  --beige:#f5dfbf;
  --black:#0d0d0d;
}
*{margin:0;padding:0;box-sizing:border-box}
html,body{width:1200px;height:3181px;overflow:hidden;background:var(--bg)}
body{font-family:"Montserrat",sans-serif;color:var(--ink)}
.band{position:relative;width:1200px;height:795px}
.band:last-child{height:796px}
.page{position:absolute;background:var(--paper);overflow:hidden}
.photo{position:absolute}
.display{font-family:"Dela Gothic One",sans-serif;line-height:.95;text-transform:uppercase}
.script{font-family:"Sacramento",cursive}

/* Cover */
.cover{left:330px;top:28px;width:540px;height:740px}
.cover-head{position:absolute;left:0;top:0;width:540px;height:250px;background:var(--paper)}
.cover-title{position:absolute;left:36px;top:36px;font-size:70px;color:var(--green)}
.cover-sub{position:absolute;left:36px;top:186px;font-size:38px;color:var(--ink)}
.cover-motto{position:absolute;right:34px;top:46px;width:118px;height:118px;border:2px solid var(--green);border-radius:50%;display:flex;align-items:center;justify-content:center;text-align:center;color:var(--green);font-size:24px;line-height:.9}
.cover-photo{left:0;top:250px;width:540px;height:490px;background:radial-gradient(circle at 60% 45%,#e9dccb 0,#b98a5e 18%,#5a3a22 45%,#2e1e14 100%)}
.cover-brand{position:absolute;left:30px;bottom:30px;padding:16px 18px;background:var(--paper);font-size:17px;font-weight:700;color:var(--ink)}

/* Spreads */
.left{left:100px;top:58px;width:500px;height:680px}
.right{left:600px;top:58px;width:500px;height:680px}
.spread-shadow{position:absolute;left:598px;top:58px;width:4px;height:680px;background:rgba(0,0,0,.12);z-index:2}
.big-title{position:absolute;font-size:58px}
.kicker{font-size:11px;color:var(--muted)}
.sec-title{font-size:22px;margin-top:2px;margin-bottom:14px}
.sec-title .accent{display:block}
.menu-block{position:absolute}
.item{margin-bottom:14px}
.item-row{display:flex;justify-content:space-between;align-items:baseline;font-size:11px;font-weight:700}
.item-row .price{font-weight:400;font-size:10px}
.item-desc{font-size:9px;color:var(--muted);line-height:1.35;max-width:88%}
.drink{display:flex;align-items:baseline;font-size:9.5px;color:#444;margin-bottom:3px}
.drink .dots{flex:1;border-bottom:1px dotted #999;margin:0 4px}
.mood{position:absolute;text-align:center;font-size:17px;line-height:1.05;padding:14px 0;border-top:3px solid;border-bottom:3px solid}

.c-orange{color:var(--orange)}
.c-green{color:var(--green)}
.c-yellow{color:var(--yellow)}
</style>
</head>
<body>

<!-- Cover -->
<section class="band">
  <div class="page cover">
    <div class="cover-head">
      <div class="display cover-title">Bistro<br>&amp;Café</div>
      <div class="display cover-sub">Zum Hammerwerk</div>
      <div class="script cover-motto">good mood after<br>good food</div>
    </div>
    <div class="photo cover-photo" role="img" aria-label="Zwei Tassen Cappuccino mit Latte Art auf einem Holztisch, daneben Rosmarin"></div>
    <div class="cover-brand">Zum Hammerwerk</div>
  </div>
</section>

<!-- Kaffee & Kuchen -->
<section class="band">
  <div class="page left">
    <div class="photo" style="inset:0;background:linear-gradient(180deg,#6b4a30 0,#9a7352 40%,#e7e2dc 62%,#d6cfc6 100%)" role="img" aria-label="Waffeln mit Sirup und Heidelbeeren auf einem Teller"></div>
    <div class="display big-title c-orange" style="left:120px;top:40px">Kaffee<br><span style="color:#fff">&amp;</span>Kuchen</div>
  </div>
  <div class="spread-shadow"></div>
  <div class="page right">
    <div class="menu-block" style="left:40px;top:40px;width:230px">
      <div class="kicker">Cake &amp; Waffles</div>
      <div class="display sec-title">Sweet<span class="accent c-orange">Party</span></div>
      <div class="item"><div class="item-row"><span>The Big Bro</span><span class="price">€ 2,30</span></div><div class="item-desc">Frisch gebacken mit Sahne und Kirschen</div></div>
      <div class="item"><div class="item-row"><span>The Big Bro</span><span class="price">€ 2,30</span></div><div class="item-desc">Mit warmem Ahornsirup und frischen Beeren</div></div>
      <div class="item"><div class="item-row"><span>The Big Bro</span><span class="price">€ 2,30</span></div><div class="item-desc">Hausgemacht, dazu Vanilleeis und heiße Schokosauce</div></div>
    </div>
    <div class="photo" style="left:300px;top:40px;width:170px;height:150px;background:linear-gradient(135deg,#c9a57a,#6d4d33 60%,#e6ddd2)" role="img" aria-label="Frühstückstisch mit Kaffee, Orangensaft und Croissants"></div>
    <div style="position:absolute;left:290px;top:190px;width:180px;height:460px;background:var(--beige)"></div>
    <div class="menu-block" style="left:300px;top:225px;width:165px">
      <div class="kicker">Frühstück</div>
      <div class="display sec-title">Good<span class="accent c-orange">Morning</span></div>
      <div class="item"><div class="item-row"><span>The Big Bro</span><span class="price">€ 2,30</span></div><div class="item-desc">Brötchen, Butter, Marmelade und frischer Kaffee</div></div>
      <div class="item"><div class="item-row"><span>The Big Bro</span><span class="price">€ 2,30</span></div><div class="item-desc">Zwei Spiegeleier mit Speck und Toast</div></div>
      <div class="item"><div class="item-row"><span>The Big Bro</span><span class="price">€ 2,30</span></div><div class="item-desc">Joghurt mit Granola, Honig und Obst</div></div>
      <div class="item"><div class="item-row"><span>The Big Bro</span><span class="price">€ 2,30</span></div><div class="item-desc">Croissant, Orangensaft und ein großer Cappuccino</div></div>
    </div>
    <div class="menu-block" style="left:40px;top:300px;width:220px">
      <div class="kicker">Coffe</div>
      <div class="display sec-title">Wake<span class="accent c-orange">Me Up</span></div>
      <div class="script c-orange" style="position:absolute;left:110px;top:-6px;width:80px;height:80px;border:1.5px solid var(--orange);border-radius:50%;display:flex;align-items:center;justify-content:center;text-align:center;font-size:17px;line-height:.9">life begins after coffee</div>
      <div class="drink"><span>0,3 l Vulkan Cola</span><span class="dots"></span><span>€ 2,30</span></div>
      <div class="drink"><span>0,3 l Vulkan Cola Zero</span><span class="dots"></span><span>€ 2,30</span></div>
      <div class="drink"><span>0,3 l Maarbrause Mate</span><span class="dots"></span><span>€ 2,30</span></div>
      <div class="drink"><span>0,3 l Maarbrause Orange</span><span class="dots"></span><span>€ 2,30</span></div>
      <div class="drink"><span>0,3 l Maarbrause ohne Zucker</span><span class="dots"></span><span>€ 2,30</span></div>
    </div>
  </div>
</section>

<!-- Burger & Soßen -->
<section class="band">
  <div class="page left">
    <div class="menu-block" style="left:40px;top:50px;width:190px">
      <div class="kicker">Burger</div>
      <div class="display sec-title"><span class="accent c-green">Mouth</span>Meating</div>
      <div class="item"><div class="item-row"><span>The Big Bro</span><span class="price">€ 2,30</span></div><div class="item-desc">Rindfleisch, Cheddar, Zwiebeln und hausgemachte Sauce</div></div>
      <div class="item"><div class="item-row"><span>The Big Bro</span><span class="price">€ 2,30</span></div><div class="item-desc">Doppeltes Patty mit Bacon und BBQ</div></div>
      <div class="item"><div class="item-row"><span>The Big Bro</span><span class="price">€ 2,30</span></div><div class="item-desc">Pulled Pork, Krautsalat und rauchige Sauce</div></div>
      <div class="item"><div class="item-row"><span>The Big Bro</span><span class="price">€ 2,30</span></div><div class="item-desc">Hähnchen knusprig, Salat und Honigsenf Dip</div></div>
    </div>
    <div style="position:absolute;left:243px;top:60px;width:1px;height:240px;background:#ddd"></div>
    <div class="menu-block" style="left:260px;top:50px;width:200px">
      <div class="kicker">Veggy Burger</div>
      <div class="display sec-title"><span class="accent c-green">Healthy</span>Tasty</div>
      <div class="item"><div class="item-row"><span>The Big Bro</span><span class="price">€ 2,30</span></div><div class="item-desc">Linsenpatty mit Spinat und Avocado Creme</div></div>
      <div class="item"><div class="item-row"><span>The Big Bro</span><span class="price">€ 2,30</span></div><div class="item-desc">Halloumi, gegrillte Paprika und frischer Rucola</div></div>
      <div class="item"><div class="item-row"><span>The Big Bro</span><span class="price">€ 2,30</span></div><div class="item-desc">Süßkartoffel, Rotkohl und eine würzige Joghurtsauce</div></div>
      <div class="item"><div class="item-row"><span>The Big Bro</span><span class="price">€ 2,30</span></div><div class="item-desc">Pilzpatty mit Zwiebeln und Kräuter Mayo</div></div>
    </div>
    <div style="position:absolute;left:30px;top:405px;width:205px;height:165px;background:var(--green)"></div>
    <div class="photo" style="left:45px;top:385px;width:215px;height:165px;background:linear-gradient(135deg,#f1e6d8,#e3b77a 50%,#c86a3a)" role="img" aria-label="Junge Frau beißt lachend in einen Burger"></div>
    <div class="display mood c-green" style="left:300px;top:430px;width:80px;border-color:var(--green)">Mood<br>for<br>Food</div>
  </div>
  <div class="spread-shadow"></div>
  <div class="page right" style="background:var(--black)">
    <div class="photo" style="left:0;top:0;width:500px;height:430px;background:radial-gradient(circle at 50% 45%,#d79a52 0,#7b4a26 30%,#3a2a1e 60%,#0d0d0d 100%)" role="img" aria-label="Burger mit Sesambrötchen, Spinat und Zwiebeln auf einem Holzbrett"></div>
    <div class="display big-title c-green" style="left:40px;top:500px;font-size:60px">Burger<br><span style="color:#fff">&amp;</span>Soßen</div>
  </div>
</section>

<!-- Cocktails & Wein -->
<section class="band">
  <div class="page left">
    <div class="photo" style="inset:0;background:radial-gradient(circle at 55% 50%,#c9cf8a 0,#7b7a3c 25%,#3b3324 55%,#1c1712 100%)" role="img" aria-label="Cocktail mit Limetten und Minze auf einer Holzscheibe"></div>
    <div class="display big-title c-yellow" style="left:40px;top:50px">Cocktails<br><span style="color:#fff">&amp;</span>Wein</div>
  </div>
  <div class="spread-shadow"></div>
  <div class="page right">
    <div class="menu-block" style="left:40px;top:40px;width:200px">
      <div class="kicker">Cocktails</div>
      <div class="display sec-title">Shake it,<span class="accent c-yellow">Baby</span></div>
      <div class="drink"><span>0,3 l Vulkan Cola</span><span class="dots"></span><span>€ 2,30</span></div>
      <div class="drink"><span>0,3 l Vulkan Cola Zero</span><span class="dots"></span><span>€ 2,30</span></div>
      <div class="drink"><span>0,3 l Maarbrause Mate</span><span class="dots"></span><span>€ 2,30</span></div>
      <div class="drink"><span>0,3 l Maarbrause Orange</span><span class="dots"></span><span>€ 2,30</span></div>
      <div class="drink"><span>0,3 l Maarbrause Zitrone</span><span class="dots"></span><span>€ 2,30</span></div>
      <div class="drink"><span>0,3 l Eifeler Apfelschorle</span><span class="dots"></span><span>€ 2,30</span></div>
    </div>
    <div class="menu-block" style="left:40px;top:260px;width:200px">
      <div class="kicker">Non Alkoholic</div>
      <div class="display sec-title">Fresh<span class="accent c-yellow">and cool</span></div>
      <div class="drink"><span>0,3 l Vulkan Cola</span><span class="dots"></span><span>€ 2,30</span></div>
      <div class="drink"><span>0,3 l Vulkan Cola Zero</span><span class="dots"></span><span>€ 2,30</span></div>
      <div class="drink"><span>0,3 l Maarbrause Mate</span><span class="dots"></span><span>€ 2,30</span></div>
      <div class="drink"><span>0,3 l Maarbrause Orange</span><span class="dots"></span><span>€ 2,30</span></div>
      <div class="drink"><span>0,3 l Maarbrause ohne Zucker</span><span class="dots"></span><span>€ 2,30</span></div>
      <div class="kicker" style="margin-top:18px;margin-bottom:6px">Alkoholic</div>
      <div class="drink"><span>0,3 l Pils vom Fass</span><span class="dots"></span><span>€ 2,30</span></div>
      <div class="drink"><span>0,3 l Radler</span><span class="dots"></span><span>€ 2,30</span></div>
      <div class="drink"><span>0,3 l Weizen</span><span class="dots"></span><span>€ 2,30</span></div>
      <div class="drink"><span>0,2 l Hauswein</span><span class="dots"></span><span>€ 2,30</span></div>
      <div class="drink"><span>0,2 l Eifeler Apfelwein</span><span class="dots"></span><span>€ 2,30</span></div>
    </div>
    <svg style="position:absolute;left:380px;top:30px" width="86" height="86" viewBox="0 0 86 86" aria-hidden="true"><circle cx="43" cy="43" r="40" fill="none" stroke="var(--yellow)" stroke-width="3"/></svg>
    <div class="menu-block" style="left:270px;top:130px;width:195px">
      <div class="kicker">Wine</div>
      <div class="display sec-title">Cheer<span class="accent c-yellow">me up</span></div>
      <div class="drink"><span>0,2 l Riesling trocken</span><span class="dots"></span><span>€ 2,30</span></div>
      <div class="drink"><span>0,2 l Grauburgunder</span><span class="dots"></span><span>€ 2,30</span></div>
      <div class="drink"><span>0,2 l Rosé</span><span class="dots"></span><span>€ 2,30</span></div>
      <div class="drink"><span>0,2 l Spätburgunder</span><span class="dots"></span><span>€ 2,30</span></div>
      <div class="drink"><span>0,2 l Dornfelder</span><span class="dots"></span><span>€ 2,30</span></div>
      <div class="drink"><span>0,2 l Weinschorle</span><span class="dots"></span><span>€ 2,30</span></div>
      <div class="drink"><span>0,2 l Eifeler Apfelsecco</span><span class="dots"></span><span>€ 2,30</span></div>
    </div>
    <div class="display mood c-yellow" style="left:320px;top:440px;width:100px;border-color:var(--yellow);border-top:none">Mood<br>for<br>Drinks</div>
  </div>
</section>

</body>
</html>
```